Design my dad a new business card because his current one sucks!

I need a business card designed for my fathers home maintenance business. His customers are individuals (single moms, old people etc.) as well as the occasional business. As such it needs to be accessible to both target audiences.

The front of the card should be dark grey on yellow with the logo and contain the following information:
- Darren Whitlock
- 0488 372 915
- info@bluegumhomecare.example.au
- 0488 372 915

- ABN: 71 284 630 912
- 'Fully Insured'

The reverse should be yellow on dark grey and will have the web address:
- bluegumhomecare.example.au

And a few key services he offers:
GENERAL REPAIRS
PAINTING/TILING/
PAVING &CONCRETING
PRESSURE WASHING
ON-SITE WELDING
DECKING ADDITIONS & REPAIRS
FENCING
FULL BOND CLEANING

This will be first time the logo has been printed so you will need to come up with the best CMYK approximation of the RGB colours to make sure it is a close as possible.

```html
<!DOCTYPE html>
<html lang="en">
<head>
<meta charset="utf-8">
<title>Bluegum Home Care – Business Card</title>
<link rel="stylesheet" href="https://fonts.googleapis.com/css2?family=Indie+Flower&family=Oswald:wght@400&display=swap">
<style>
  :root {
    --page: #ffffff;
    --card-yellow: #f9e700;
    --ink-grey: #58585a;
  }
  * { margin: 0; padding: 0; box-sizing: border-box; }
  html, body {
    width: 1200px;
    height: 900px;
    overflow: hidden;
    background: var(--page);
  }
  .canvas {
    position: relative;
    width: 1200px;
    height: 900px;
    background: var(--page);
  }
  .card-front {
    position: absolute;
    left: 0;
    top: 123px;
    width: 1200px;
    height: 665px;
    background: var(--card-yellow);
    color: var(--ink-grey);
    font-family: "Indie Flower", cursive;
  }
  .owner-name {
    position: absolute;
    left: 34px;
    top: 66px;
    font-size: 54px;
    line-height: 1;
    font-weight: 400;
    letter-spacing: 1px;
  }
  .brand {
    position: absolute;
    right: 36px;
    top: 242px;
    display: flex;
    align-items: center;
    gap: 22px;
  }
  .brand-dot {
    width: 58px;
    height: 58px;
    border-radius: 50%;
    background: var(--ink-grey);
  }
  .brand-name {
    font-size: 70px;
    line-height: 1;
    font-weight: 400;
  }
  .contact-list {
    position: absolute;
    left: 34px;
    top: 472px;
    list-style: none;
  }
  .contact-item {
    display: flex;
    align-items: center;
    height: 64px;
    margin-bottom: 16px;
    font-size: 46px;
    line-height: 1;
  }
  .contact-item.email { font-size: 40px; }
  .contact-icon {
    width: 60px;
    height: 48px;
    margin-right: 24px;
    flex: none;
  }
  .business-details {
    position: absolute;
    left: 876px;
    top: 500px;
    font-family: "Oswald", sans-serif;
    font-size: 38px;
    line-height: 58px;
    letter-spacing: 0.5px;
  }
</style>
</head>
<body>
<div class="canvas">
  <section class="card-front">
    <h1 class="owner-name">Darren Whitlock</h1>

    <div class="brand">
      <span class="brand-dot"></span>
      <span class="brand-name">Bluegum Home Care</span>
    </div>

    <ul class="contact-list">
      <li class="contact-item phone">
        <svg class="contact-icon" viewBox="0 0 60 48" aria-hidden="true">
          <path d="M2 14 C2 4 58 4 58 14 L58 18 L44 18 L44 12 L16 12 L16 18 L2 18 Z" fill="#58585a"/>
          <path d="M14 20 L46 20 L54 46 L6 46 Z" fill="#58585a"/>
          <g fill="#f9e700">
            <rect x="23" y="25" width="4" height="4"/><rect x="29" y="25" width="4" height="4"/><rect x="35" y="25" width="4" height="4"/>
            <rect x="23" y="31" width="4" height="4"/><rect x="29" y="31" width="4" height="4"/><rect x="35" y="31" width="4" height="4"/>
            <rect x="23" y="37" width="4" height="4"/><rect x="29" y="37" width="4" height="4"/><rect x="35" y="37" width="4" height="4"/>
          </g>
        </svg>
        <span>0488 372 915</span>
      </li>
      <li class="contact-item email">
        <svg class="contact-icon" viewBox="0 0 60 48" aria-hidden="true">
          <g fill="none" stroke="#58585a" stroke-width="3">
            <rect x="6" y="8" width="48" height="34"/>
            <path d="M6 8 L30 28 L54 8"/>
            <path d="M6 42 L24 24 M54 42 L36 24"/>
          </g>
        </svg>
        <span>info@bluegumhomecare.example.au</span>
      </li>
    </ul>

    <div class="business-details">
      <p class="abn">ABN: 71 284 630 912</p>
      <p class="insured">‘Fully Insured’</p>
    </div>
  </section>
</div>
</body>
</html>
```